Wireframes of In Store Preview

We need to simplify our in store preview capability. For this particular project what I really need are wireframes for the in store preview form, which is currently several pages - but needs to be condensed. The current Free In-Store Preview process is divided over five pages and is closely tied to the process of purchasing a product. This project simplifies the process and highlights the “no obligation to buy” value proposition of the feature.
Objectives
Simplify the Free In Store Preview (FISP) reservation process. We believe that reducing the number of pages required to complete the reservation process will reduce abandonment. Currently there is a 80+% drop off between the FISP - Edit page and the FISP - Review page. Some of this is to be expected, but we feel that if we can do the following that we can reduce some of that drop-off:
1. highlight the “no obligation to buy” and “see it in person” aspects of FISP
2. Remove the Lumbrel Financing option from the payment method form - the CC is only needed to secure the reservation, so having this option here implies that this method is the final form of payment. During the final purchase the customer can choose to use Financing instead.
3. Remove selection of Protection Plan, deferring that to the post-reservation sale, which can provide a better hands-on, concierge experience.
4. reduce the steps from 5 steps to 2.
Here is the current flow:
1. Click Free In Store Preview on the PDP
2. A pop-up displays with the ring size and insurance option - the customer has to choose to preview it again 😔 Edit, Review and then Thank you) to 2 steps (edit/review and then thank you)
3. the form is displayed with the store location and credit card information
4. the review page is displayed on which the customer needs to finalize
5. the thank you page displays
Here is the new flow I’d like to get wireframes for:
* Click Free In Store Preview on the PDP (I don’t need a wireframe for this)
* the form is displayed with the store location and credit card form - once the customer enters their information they can finalize the reservation
* the thank you page displays
I’ve included screenshots of the current flow here. Also - FYI - as an example, I think Dorsel Quint does a good job of communicating that their Porch Sample Kit option is free even though they do require a credit card authorization to complete the transaction. Also, their core user base is Millenial - just like ours. (I know, you wouldn't know it from our current website! :-) Anyway - I like their cleaner more tech saavy form behavior. So, don't be shy about moving away from the overcrowded multi-step form pages we have now.
Lastly - if you want to try the flow yourself - you can follow these steps:
1. Click here: https://www.velmoro.example/engagement-rings/solitaire-diamond-gallery-engagement-ring-in-14kt-white-gold/19815
2. On the setting PDP page here - click the CHOOSE THIS RING button.
3. That will take you to the diamond inventory where you need to select a diamond. Choose any diamond and “add it to your engagement ring” - this will take you to the configured ring PDP
4. Click the FREE IN STORE PREVIEW option on the configured ring PDP - a pop up will display
5. On the pop up, select the ring size (I know, I know - even if you selected one before you’ll need to select it again, this is a bug) and then click the PREVIEW THIS RING button. This will take you to the Free-in-store preview page form.
6. On the free in store preview page, enter a credit card payment method and hit the CONTINUE button. I promise - your card will NOT be charged if you hit this button. This will take you to the Review page.
7. On the Review Page you should STOP. PLEASE DO NOT PROCEED PAST THIS POINT. Please refer to the comp for the thank you page.
Thanks!
Target Market(s)
Millenial Engagement Ring Shoppers
Industry/Entity Type
Store
Number of Pages Required
2 page
Look and feel
Each slider illustrates characteristics of the customer's brand and the style your logo design should communicate.

```html
<!DOCTYPE html>
<html lang="en">
<head>
<meta charset="utf-8">
<title>Velmoro – Free In-Store Preview</title>
<link href="https://fonts.googleapis.com/css2?family=Poppins:wght@400;500;600;700&display=swap" rel="stylesheet">
<style>
  :root{
    --gold:#e3b321;
    --gold-text:#d9a91a;
    --ink:#222222;
    --muted:#a3a3a3;
    --line:#ecd27a;
    --field:#a6a6a6;
    --box-border:#dcdcdc;
    --footer:#ececec;
    --bg:#ffffff;
  }
  *{box-sizing:border-box;margin:0;padding:0}
  html,body{width:1200px;height:1200px;overflow:hidden;background:var(--bg);font-family:'Poppins',sans-serif}
  .page{position:absolute;left:303px;top:42px;width:596px;height:1117px;background:#fff;box-shadow:0 4px 24px rgba(0,0,0,.12);overflow:hidden}
  .abs{position:absolute}
  .header-phone{left:76px;top:15px;font-size:5px;font-weight:500;color:var(--ink)}
  .brand{left:0;width:596px;top:11px;display:flex;justify-content:center;align-items:center;gap:5px}
  .brand-dot{width:14px;height:14px;border-radius:50%;background:var(--gold)}
  .brand-name{font-size:13px;font-weight:600;letter-spacing:3px;color:var(--ink)}
  .header-account{right:75px;top:15px;font-size:5px;color:var(--ink)}
  .hero{left:0;top:37px;width:596px;height:56px;background:linear-gradient(90deg,#5a5657 0%,#8a7477 35%,#9a7f83 60%,#6b6667 100%)}
  .hero-title{left:0;width:596px;top:67px;text-align:center;color:#fff;font-size:8.5px;font-weight:600;line-height:1}
  .crumbs{left:74px;top:119px;font-size:4.5px;color:var(--ink)}
  .crumbs span{color:var(--gold-text)}
  .section-title{left:0;width:596px;text-align:center;color:var(--gold-text);font-weight:600}
  .title-info{top:118px;font-size:9px}
  .ornament{left:268px;top:131px}
  .product-photo{left:74px;top:159px;width:139px;height:139px;border:1px solid var(--box-border);background:radial-gradient(circle at 50% 45%,#e9eaee 0%,#ffffff 55%)}
  .item-name{left:247px;font-size:7px;font-weight:500;color:var(--ink)}
  .item-sub{left:247px;font-size:4.5px;color:var(--muted)}
  .rule{height:1px;background:var(--line)}
  .total-label{left:244px;top:333px;font-size:5px;font-weight:700;color:var(--ink)}
  .total-label small{font-size:3px;font-weight:400;color:var(--muted)}
  .total-price{right:75px;top:333px;font-size:5px;font-weight:500;color:var(--gold-text)}
  .title-reserve{top:382px;font-size:7px}
  .reserve-bar{left:288px;top:396px;width:20px;height:1px;background:var(--gold)}
  .reserve-copy{left:170px;width:256px;top:406px;text-align:center;font-size:5px;line-height:7px;color:var(--muted)}
  .form-band{left:0;top:449px;width:596px;height:383px;background:linear-gradient(110deg,#1e1e1f 0%,#2c2d33 30%,#48484a 60%,#5b5b5c 100%)}
  .form-label{font-size:5px;font-weight:600;color:#fff}
  .field{height:18px;background:var(--field);font-size:6px;color:#fff;padding:5px 4px;line-height:1}
  .select-arrow{position:absolute;right:0;top:3px;width:10px;height:12px;border-left:1px solid #ddd}
  .select-arrow::after{content:"";position:absolute;left:2px;top:5px;border:3px solid transparent;border-top:4px solid #fff}
  .form-divider{left:186px;top:681px;width:223px;height:1px;background:#8a8a8a}
  .help{right:198px;top:703px;font-size:4px;color:#fff}
  .continue{left:234px;top:783px;width:116px;height:21px;background:var(--gold);color:#fff;font-size:6.5px;font-weight:600;display:flex;align-items:center;justify-content:center}
  .benefit{top:867px;width:126px;height:90px;border:1px solid var(--box-border);text-align:center}
  .benefit svg{margin-top:11px}
  .benefit h3{font-size:6px;font-weight:500;color:var(--gold-text);margin-top:4px}
  .benefit p{font-size:4.3px;line-height:8px;color:var(--muted);padding:2px 12px 0}
  .detail{top:1000px;width:118px;text-align:center}
  .detail h4{font-size:5.6px;font-weight:500;color:var(--gold-text)}
  .detail p{font-size:4.8px;line-height:6.5px;color:var(--muted);margin-top:8px}
  .detail-sep{top:996px;width:1px;height:41px;background:#e2e2e2}
  .footer{left:0;top:1066px;width:596px;height:51px;background:var(--footer);text-align:center;padding-top:9px;font-size:4.6px;line-height:7px;color:#8a8a8a}
  .footer a{display:block;color:var(--ink);text-decoration:none;font-weight:500;line-height:6.5px}
</style>
</head>
<body>
<main class="page">
  <header>
    <div class="abs header-phone">1.888.555.0142</div>
    <div class="abs brand"><span class="brand-dot"></span><span class="brand-name">VELMORO</span></div>
    <div class="abs header-account">MY ACCOUNT</div>
  </header>

  <div class="abs hero" role="img" aria-label="Photo of a diamond halo ring resting on a pink and white striped gift box"></div>
  <h1 class="abs hero-title">FREE IN-STORE PREVIEW</h1>

  <nav class="abs crumbs"><span>RESERVATIN INFO</span>/ REVIEW RESERVATION</nav>
  <h2 class="abs section-title title-info">RESERVATION INFO</h2>
  <svg class="abs ornament" width="60" height="6" viewBox="0 0 60 6" aria-hidden="true">
    <line x1="0" y1="3" x2="26" y2="3" stroke="#e3b321" stroke-width="1"/>
    <line x1="34" y1="3" x2="60" y2="3" stroke="#e3b321" stroke-width="1"/>
    <circle cx="30" cy="3" r="2.2" fill="none" stroke="#e3b321" stroke-width="0.8"/>
  </svg>

  <div class="abs product-photo" role="img" aria-label="Product photo of a white gold engagement ring with an oval sapphire and diamond halo"></div>

  <div class="abs item-name" style="top:193px">Solitaire Diamond Engagement Ring</div>
  <div class="abs item-sub" style="top:207px">In 14kt White Gold (0.10 CTW) for a Round Center</div>
  <div class="abs rule" style="left:247px;top:229px;width:274px"></div>
  <div class="abs item-name" style="top:244px">Diamond</div>
  <div class="abs item-sub" style="top:258px">0.62 Carat Ideal Cut Round Diamond</div>

  <div class="abs rule" style="left:74px;top:322px;width:447px"></div>
  <div class="abs total-label">TOTAL <small>(including all fees)</small></div>
  <div class="abs total-price">$2,937.00</div>
  <div class="abs rule" style="left:74px;top:349px;width:447px"></div>

  <h2 class="abs section-title title-reserve">RESERVE YOUR FREE PREVIEW</h2>
  <div class="abs reserve-bar"></div>
  <p class="abs reserve-copy">"Neque porro quisquam est qui dolorem ipsum quia dolor sit amet, consectetur, adipisci velit..."</p>

  <section class="abs form-band" role="img" aria-label="Dark photo of a ring in an open jewelry box"></section>

  <div class="abs form-label" style="left:186px;top:471px">FIRST NAME</div>
  <div class="abs form-label" style="left:294px;top:471px">LAST NAME</div>
  <div class="abs field" style="left:186px;top:481px;width:105px"></div>
  <div class="abs field" style="left:294px;top:481px;width:104px"></div>

  <div class="abs form-label" style="left:186px;top:506px">STREET ADDRESS</div>
  <div class="abs field" style="left:186px;top:515px;width:212px"></div>
  <div class="abs field" style="left:186px;top:538px;width:212px"></div>

  <div class="abs form-label" style="left:186px;top:564px">CITY</div>
  <div class="abs form-label" style="left:260px;top:564px">STATE</div>
  <div class="abs form-label" style="left:334px;top:564px">ZIP</div>
  <div class="abs field" style="left:186px;top:574px;width:65px"></div>
  <div class="abs field" style="left:260px;top:574px;width:65px"><span class="select-arrow"></span></div>
  <div class="abs field" style="left:334px;top:574px;width:64px"></div>

  <div class="abs form-label" style="left:186px;top:598px">BILLING PHONE</div>
  <div class="abs form-label" style="left:270px;top:598px">CONTACT PHONE</div>
  <div class="abs field" style="left:186px;top:607px;width:71px">( ) -</div>
  <div class="abs field" style="left:270px;top:607px;width:71px">( ) -</div>

  <div class="abs form-label" style="left:186px;top:633px">EMAIL</div>
  <div class="abs field" style="left:186px;top:642px;width:212px"></div>

  <div class="abs form-divider"></div>

  <div class="abs form-label" style="left:186px;top:698px">CREDIT CARD NUMBER</div>
  <div class="abs form-label" style="left:334px;top:698px">CVV</div>
  <div class="abs help">Help?</div>
  <div class="abs field" style="left:186px;top:708px;width:139px"></div>
  <div class="abs field" style="left:334px;top:708px;width:64px"></div>

  <div class="abs form-label" style="left:186px;top:735px">EXP. MONTH</div>
  <div class="abs form-label" style="left:334px;top:735px">EXP. YEAR</div>
  <div class="abs field" style="left:186px;top:745px;width:139px"></div>
  <div class="abs field" style="left:334px;top:745px;width:64px"><span class="select-arrow"></span></div>

  <div class="abs continue">CONTINUE</div>

  <div class="abs benefit" style="left:75px">
    <svg width="22" height="22" viewBox="0 0 24 24" fill="none" stroke="#e3b321" stroke-width="1.4" aria-hidden="true">
      <path d="M3 11a9 8 0 0 1 18 0"/><path d="M3 11q3-2 6 0q3-2 6 0q3-2 6 0"/>
      <path d="M3 11l8 9M21 11l-8 9M9 11l2 9M15 11l-2 9"/><rect x="10.5" y="19.5" width="3" height="2.5"/>
    </svg>
    <h3>NO RISK</h3>
    <p>"Neque porro quisquam est qui dolor-em ipsum quia dolor sit amet, con-sectetur, adipisci velit..."</p>
  </div>
  <div class="abs benefit" style="left:237px">
    <svg width="22" height="22" viewBox="0 0 24 24" fill="none" stroke="#e3b321" stroke-width="1.4" aria-hidden="true">
      <path d="M6 17V11a6 6 0 0 1 12 0v6l2 2H4z"/><path d="M10 21a2 2 0 0 0 4 0"/><path d="M12 3v2"/>
    </svg>
    <h3>A FRIENDLY REMAINDER</h3>
    <p>"Neque porro quisquam est qui dolor-em ipsum quia dolor sit amet, con-sectetur, adipisci velit..."</p>
  </div>
  <div class="abs benefit" style="left:396px">
    <svg width="22" height="22" viewBox="0 0 24 24" aria-hidden="true">
      <path fill="#e3b321" d="M13 2l1.6 3.3 3.6.5-2.6 2.5.6 3.6L13 10.2l-3.2 1.7.6-3.6-2.6-2.5 3.6-.5z"/>
      <rect x="2" y="14" width="4" height="7" fill="#e3b321"/>
      <path fill="#e3b321" d="M7 14h5l2 2h5a2 2 0 0 1 0 3l-5 2H7z"/>
    </svg>
    <h3>SUPERIOR SERVICE</h3>
    <p>"Neque porro quisquam est qui dolor-em ipsum quia dolor sit amet, con-sectetur, adipisci velit..."</p>
  </div>

  <div class="abs detail" style="left:62px"><h4>ESTIMATED PREVIEW PERIOD</h4><p>Mon, Aug 28 - Thu, Sep 03</p></div>
  <div class="abs detail-sep" style="left:191px"></div>
  <div class="abs detail" style="left:190px"><h4>YOUR PREVIEW LOACATION</h4><p>Lorem Ipsum is simply<br>dummy text</p></div>
  <div class="abs detail-sep" style="left:311px"></div>
  <div class="abs detail" style="left:310px"><h4>VARIFICATION METHOD</h4><p>Lorem Ipsum is simply<br>dummy text</p></div>
  <div class="abs detail-sep" style="left:431px"></div>
  <div class="abs detail" style="left:424px"><h4>BELLING ADDRESS</h4><p>Lorem Ipsum is simply<br>dummy text</p></div>

  <footer class="abs footer">
    2017 VELMORO ALL RIGHTS RESERVED
    <a href="#">Terms &amp; Conditions</a>
    <a href="#">Privacy Policy</a>
  </footer>
</main>
</body>
</html>
```